GLP letterhead

We need a letterhead design for our new company based in Los Angeles called "Gold Lantern Pictures". We develop film and television projects. We work with investors, financiers, film production companies, film distribution and sales companies as well as studios. We would like to incorporate our logo (see attached) but make the letterhead simple and elegant. We need to include: logo, company address, phone number and company website.
Updates

Hello designers, Thanks for your submissions. For our letterhead, we are looking for something more simple and elegant. No heavy bars or lines. Make it feel light and clean. Not a lot of ink on the page. Use the logo and contact info but think "clean", "streamlined" and mostly white paper. Looking forward to seeing more... thanks! Gold Lantern Pictures team

Target Market(s)

Studio executives, talent agents and agencies, financiers, investors.

Industry/Entity Type

It Company

Requirements
Must have
• Gold Lantern Pictures logo (see attached). Logo may be cropped and altered appropriately for elegant letterhead design.
• Please include:
• COMPANY ADDRESS:
• Ridgeway Studio Park
• 2850 Halverson Street
• Tower Annex, 4th Floor
• Manhattan Beach, CA 90412
• COMPANY WEBSITE:
• www.goldlanternpicturesco.example
• COMPANY PHONE NUMBER:
• 310-555-0148

```html
<!DOCTYPE html>
<html lang="en">
<head>
<meta charset="utf-8">
<title>Gold Lantern Pictures — Letterhead</title>
<link href="https://fonts.googleapis.com/css2?family=Oswald:wght@300;400;500&display=swap" rel="stylesheet">
<style>
  :root {
    --backdrop: #e6e6e6;
    --paper: #ffffff;
    --brand: #1f7fb6;
    --ink: #2a2a2a;
    --rule: #3a3a3a;
    --mark: #222c33;
  }
  * { margin: 0; padding: 0; box-sizing: border-box; }
  html, body {
    width: 1200px;
    height: 795px;
    overflow: hidden;
    background: var(--backdrop);
    font-family: "Oswald", "Arial Narrow", sans-serif;
  }
  .letterhead {
    position: absolute;
    left: 333px;
    top: 20px;
    width: 534px;
    height: 755px;
    background: var(--paper);
    box-shadow: 0 2px 10px rgba(0,0,0,0.12);
  }
  .brand {
    position: absolute;
    left: 42px;
    top: 42px;
    display: flex;
    align-items: center;
    gap: 10px;
  }
  .brand-dot {
    width: 26px;
    height: 26px;
    border-radius: 50%;
    background: var(--brand);
  }
  .brand-text { display: flex; flex-direction: column; }
  .brand-name {
    font-weight: 500;
    font-size: 14px;
    letter-spacing: 2px;
    text-transform: uppercase;
    color: var(--brand);
    line-height: 1.1;
  }
  .brand-tagline {
    font-weight: 500;
    font-size: 6px;
    letter-spacing: 1.6px;
    text-transform: uppercase;
    color: var(--brand);
    margin-top: 2px;
  }
  .footer {
    position: absolute;
    left: 22px;
    right: 22px;
    bottom: 22px;
  }
  .footer-divider {
    display: flex;
    align-items: center;
    gap: 10px;
    margin: 0 8px 10px;
  }
  .footer-rule {
    flex: 1;
    height: 1px;
    background: var(--rule);
  }
  .footer-dot {
    width: 16px;
    height: 16px;
    border-radius: 50%;
    background: var(--mark);
  }
  .contact {
    display: flex;
    justify-content: space-between;
    align-items: center;
    font-weight: 400;
    font-size: 9px;
    color: var(--ink);
    white-space: nowrap;
  }
  .contact-item { display: flex; align-items: center; gap: 3px; }
  .contact-icon { width: 8px; height: 8px; fill: var(--ink); flex: none; }
</style>
</head>
<body>
  <main class="letterhead">
    <header class="brand">
      <span class="brand-dot"></span>
      <div class="brand-text">
        <span class="brand-name">Gold Lantern Pictures</span>
        <span class="brand-tagline">Film Development Company</span>
      </div>
    </header>

    <footer class="footer">
      <div class="footer-divider">
        <span class="footer-rule"></span>
        <span class="footer-dot"></span>
        <span class="footer-rule"></span>
      </div>
      <div class="contact">
        <span class="contact-item">
          <svg class="contact-icon" viewBox="0 0 10 10" aria-hidden="true"><path d="M5 0a3.6 3.6 0 0 0-3.6 3.6C1.4 6.3 5 10 5 10s3.6-3.7 3.6-6.4A3.6 3.6 0 0 0 5 0zm0 5a1.4 1.4 0 1 1 0-2.8A1.4 1.4 0 0 1 5 5z"/></svg>
          2850 Halverson St. Tower Annex 4th Fl. Manhattan Beach CA 90412
        </span>
        <span class="contact-item">
          <svg class="contact-icon" viewBox="0 0 10 10" aria-hidden="true"><path d="M2.2 0.5 3.6 0 5 2.8 3.9 3.8c.5 1 1.3 1.8 2.3 2.3L7.2 5 10 6.4 9.5 7.8C9.2 8.8 8 9.4 7 9 3.9 7.9 2.1 6.1 1 3 .6 2 1.2.8 2.2.5z"/></svg>
          310-555-0148
        </span>
        <span class="contact-item">
          <svg class="contact-icon" viewBox="0 0 10 10" aria-hidden="true"><path d="M5 0a5 5 0 1 0 0 10A5 5 0 0 0 5 0zm0 1c.6.7 1.1 1.8 1.3 3.5H3.7C3.9 2.8 4.4 1.7 5 1zM1 5.5h1.7c.1 1.3.4 2.4.9 3.2A4 4 0 0 1 1 5.5zm0-1a4 4 0 0 1 2.6-3.2c-.5.8-.8 1.9-.9 3.2H1zM5 9c-.6-.7-1.1-1.8-1.3-3.5h2.6C6.1 7.2 5.6 8.3 5 9zm1.4-.3c.5-.8.8-1.9.9-3.2H9a4 4 0 0 1-2.6 3.2zM7.3 4.5c-.1-1.3-.4-2.4-.9-3.2A4 4 0 0 1 9 4.5H7.3z"/></svg>
          www.goldlanternpicturesco.example
        </span>
      </div>
    </footer>
  </main>
</body>
</html>
```